New Architectural Firm Business Cards

New Business card to compliment previous pixel forum logo (attached). Please design a business card that is simple, modern, creative....please do not use "symbols", simply the logo and associated graphics/text. The front should contain name/address/phone/email/web address (with graphics).....back should be 100% graphic design using the logo somehow. Hoping for a two color (black and yellow) design. full bleed design, no borders

Target Market(s)

Commercial Architecture Clients

Industry/Entity Type

Architecture

Contact Information for Business Card

Please design a business card that is simple, modern, creative....please do not use "symbols", simply the logo and associated graphics/text. The front should contain name/address/phone/email/web address (with graphics).....back should be 100% graphic design using the logo somehow

Font styles to use
Sans Serif

Colors
FFF300
FFF600
FEFA6F
FFFEC7
FFFEE8

Requirements
Must have
• Clean, Modern Design
Should not have
• Stock images or "icons"

```html
<!DOCTYPE html>
<html lang="en">
<head>
<meta charset="utf-8">
<title>Pixel Forum – Business Card</title>
<link rel="stylesheet" href="https://fonts.googleapis.com/css2?family=Montserrat:wght@400;500;700&display=swap">
<style>
  :root {
    --backdrop: #e6e7e9;
    --paper: #ffffff;
    --ink: #231f20;
    --yellow: #f5c318;
    --yellow-faint: #fdf6dc;
    --white: #ffffff;
  }
  * { margin: 0; padding: 0; box-sizing: border-box; }
  html, body { width: 1200px; height: 1200px; overflow: hidden; }
  body {
    background: var(--backdrop);
    position: relative;
    font-family: "Montserrat", sans-serif;
    color: var(--ink);
  }
  .card {
    position: absolute;
    left: 246px;
    width: 708px;
    height: 404px;
    overflow: hidden;
    box-shadow: 5px 6px 6px rgba(0, 0, 0, 0.45);
  }
  /* ---------- front ---------- */
  .card-front { top: 136px; background: var(--paper); }
  .name-band {
    position: absolute;
    left: 0; top: 68px;
    width: 520px; height: 81px;
    background: var(--yellow);
    padding: 12px 0 0 30px;
  }
  .person-name {
    font-weight: 700;
    font-size: 31px;
    letter-spacing: 1px;
    line-height: 1.05;
  }
  .person-role {
    font-weight: 500;
    font-size: 19px;
    letter-spacing: 3.2px;
    line-height: 1.1;
  }
  .brand-front {
    position: absolute;
    right: 30px; top: 28px;
    display: flex;
    flex-direction: column;
    align-items: center;
    gap: 14px;
  }
  .brand-dot {
    width: 118px; height: 118px;
    border-radius: 50%;
    background: var(--yellow);
  }
  .brand-name {
    font-weight: 700;
    font-size: 21px;
    letter-spacing: 0.5px;
    color: var(--ink);
  }
  .faint-disc {
    position: absolute;
    right: 30px; top: 258px;
    width: 210px; height: 210px;
    border-radius: 50%;
    background: var(--yellow-faint);
  }
  .contact-list {
    position: absolute;
    left: 30px; top: 184px;
    list-style: none;
  }
  .contact-item {
    display: flex;
    align-items: center;
    gap: 20px;
    font-size: 18.5px;
    font-weight: 500;
    letter-spacing: 0.4px;
    height: 22px;
    margin-bottom: 21px;
  }
  .contact-item:first-child { margin-bottom: 25px; }
  .contact-icon { width: 22px; height: 22px; flex: none; }
  /* ---------- back ---------- */
  .card-back { top: 659px; background: var(--ink); }
  .back-band {
    position: absolute;
    left: 0; top: 131px;
    width: 100%; height: 87px;
    background: var(--yellow);
  }
  .back-dot {
    position: absolute;
    left: 354px; top: 174px;
    transform: translate(-50%, -50%);
    width: 210px; height: 210px;
    border-radius: 50%;
    background: var(--yellow);
    border: 16px solid var(--ink);
  }
  .brand-back {
    position: absolute;
    left: 0; top: 286px;
    width: 100%;
    text-align: center;
    font-weight: 700;
    font-size: 31px;
    letter-spacing: 0.5px;
    color: var(--white);
  }
</style>
</head>
<body>

<section class="card card-front" aria-label="Business card front">
  <div class="faint-disc" aria-hidden="true"></div>

  <div class="name-band">
    <p class="person-name">MARA ELLISON</p>
    <p class="person-role">MANAGER</p>
  </div>

  <div class="brand-front">
    <span class="brand-dot" aria-hidden="true"></span>
    <span class="brand-name">PIXEL FORUM</span>
  </div>

  <ul class="contact-list">
    <li class="contact-item">
      <svg class="contact-icon" viewBox="0 0 24 24" aria-hidden="true">
        <circle cx="12" cy="12" r="10" fill="none" stroke="#f5c318" stroke-width="2.2"/>
        <path d="M8.6 7.2l1.8-.4 1.1 2.6-1.2 1c.6 1.3 1.5 2.2 2.8 2.8l1-1.2 2.6 1.1-.4 1.8c-3.9.3-8-3.8-7.7-7.7z" fill="#f5c318"/>
      </svg>
      +12 4820 63 17
    </li>
    <li class="contact-item">
      <svg class="contact-icon" viewBox="0 0 24 24" aria-hidden="true">
        <circle cx="12" cy="12" r="11" fill="#f5c318"/>
        <path d="M6 8c2 0 3 1 2.5 3s1.5 2 1 4M13 5c0 2 2 2 3 3s-1 3 1 4M12 15c2-1 4 0 4 3" fill="none" stroke="#fff" stroke-width="1.8" stroke-linecap="round"/>
      </svg>
      www.pixelforum-studio.com
    </li>
    <li class="contact-item">
      <svg class="contact-icon" viewBox="0 0 24 24" aria-hidden="true">
        <rect x="1" y="5" width="22" height="14" fill="#f5c318"/>
        <path d="M1.5 5.5L12 13l10.5-7.5M1.5 18.5l8-6M22.5 18.5l-8-6" fill="none" stroke="#fff" stroke-width="1.4"/>
      </svg>
      hello@pixelforum.com
    </li>
    <li class="contact-item">
      <svg class="contact-icon" viewBox="0 0 24 24" aria-hidden="true">
        <path d="M12 1.5a8 8 0 0 1 8 8c0 5.5-8 13-8 13s-8-7.5-8-13a8 8 0 0 1 8-8z" fill="#f5c318"/>
        <circle cx="12" cy="9.5" r="3.2" fill="#fff"/>
      </svg>
      18 linden row harbor quarter
    </li>
  </ul>
</section>

<section class="card card-back" aria-label="Business card back">
  <div class="back-band" aria-hidden="true"></div>
  <span class="back-dot" aria-hidden="true"></span>
  <p class="brand-back">PIXEL FORUM</p>
</section>

</body>
</html>
```